Anzeigengestaltung in einem Lifestyle-Magazin für Unternehmensberatung
Zielgruppe
Wir sind eine Unternehmensberatung und wollen eine Anzeige in einem Life-Style-Magazin schalten, das von unseren Kunden herausgegeben wird.
Aufgabenstellung
Bisher haben wir kaum Printanzeigen gemacht. In diesem Fall dient die Anzeige auch eher der Kundenbindung als der Werbung, das das Magazin auf Lifestyle abzieht. Hier der Link zur letzten Ausgabe: https://www.alpmarkt-dorfegger.com/de/winter/
Das Projekt, das wir beim Kunden gemacht haben, wird hier vorgestellt: https://www.wendholt-partner.de/de/trends/beratung/prozessoptimierung-im-skiverleih (gerne das Video anschauen)
Die Anzeige soll sich nicht auf das Projekt beziehen, sondern soll folgende Komponenten beinhalten:
1. Slogan: 'Was ist teurer als Beratung? Ratlosigkeit!'
2. mini-Text: Wendholt & Partner ist eine renommierte Management- und Personalberatung in Süddeutschland
3. Logo
4. unsere Kontaktdaten
5. Social Icons von denjenigen Netzwerken, in denen man uns finden kann
Im Anhang findet Ihr unser Roll-up-Display. Das kann als Vorlage dienen. Die Anzeige muss nicht zwingend diesem Design folgen. Die Maße der Anzeige habe ich ebenfalls hochgeladen.
Druckunterlagenschluss ist 20.09. d.h. es eilt!!!
Wir freuen uns auf Eure kreativen Vorschläge :-)

```html
<!DOCTYPE html>
<html lang="de">
<head>
<meta charset="utf-8">
<title>Anzeige – Wendholt &amp; Partner</title>
<link rel="stylesheet" href="https://fonts.googleapis.com/css2?family=Open+Sans:wght@400;600;700&display=swap">
<style>
  :root {
    --stage: #cfcfcf;
    --stage-light: #e2e2e2;
    --brand-yellow: #eac52d;
    --brand-yellow-light: #f1d552;
    --wave-cream: #f6e9a6;
    --wave-pale: #faf2c8;
    --paper: #ffffff;
    --ink: #151515;
    --ink-soft: #2b2b2b;
    --text-white: #ffffff;
  }
  html, body {
    margin: 0;
    width: 1200px;
    height: 1200px;
    overflow: hidden;
  }
  body {
    background: radial-gradient(circle at 40% 30%, var(--stage-light), var(--stage));
    font-family: "Open Sans", Arial, sans-serif;
    position: relative;
  }
  .ad {
    position: absolute;
    left: 218px;
    top: 60px;
    width: 765px;
    height: 1080px;
    background: linear-gradient(115deg, var(--brand-yellow) 0%, var(--brand-yellow-light) 100%);
    overflow: hidden;
    box-shadow: 0 4px 18px rgba(0,0,0,0.18);
    color: var(--ink);
  }
  .tagline {
    position: absolute;
    right: 56px;
    top: 60px;
    margin: 0;
    font-size: 32px;
    font-weight: 400;
    letter-spacing: 0.5px;
    color: var(--ink);
  }
  .headline {
    position: absolute;
    left: 0;
    top: 258px;
    width: 100%;
    margin: 0;
    font-weight: 400;
  }
  .headline span { display: block; white-space: nowrap; }
  .headline .question-lead {
    margin-left: 122px;
    font-size: 52px;
    line-height: 60px;
    font-weight: 400;
  }
  .headline .question-key {
    margin-left: 60px;
    font-size: 88px;
    line-height: 88px;
    font-weight: 700;
    letter-spacing: -1.5px;
  }
  .headline .answer {
    margin-left: 112px;
    font-size: 92px;
    line-height: 96px;
    font-weight: 700;
    color: var(--text-white);
    letter-spacing: -1.5px;
  }
  .intro {
    position: absolute;
    left: 60px;
    top: 540px;
    width: 660px;
    margin: 0;
    font-size: 20.5px;
    line-height: 29px;
    color: var(--ink-soft);
  }
  .contact {
    position: absolute;
    left: 421px;
    top: 772px;
    font-size: 12.8px;
    line-height: 18px;
    color: var(--ink-soft);
  }
  .contact h2 {
    margin: 0 0 4px;
    font-size: 12.8px;
    font-weight: 700;
    color: var(--ink);
  }
  .contact p { margin: 0 0 12px; }
  .social {
    position: absolute;
    left: 580px;
    top: 893px;
    display: flex;
    gap: 10px;
  }
  .social span {
    width: 24px;
    height: 24px;
    background: var(--paper);
    border-radius: 3px;
  }
  .footer-wave {
    position: absolute;
    left: 0;
    bottom: 0;
    width: 765px;
    height: 160px;
  }
  .brand {
    position: absolute;
    left: 30px;
    bottom: 24px;
    display: flex;
    align-items: center;
    gap: 12px;
  }
  .brand-mark {
    width: 22px;
    height: 22px;
    background: var(--brand-yellow);
  }
  .brand-name {
    margin: 0;
    font-size: 32px;
    font-weight: 400;
    color: var(--ink-soft);
  }
  .website {
    position: absolute;
    right: 30px;
    bottom: 32px;
    margin: 0;
    font-size: 16.5px;
    font-weight: 700;
    color: var(--ink);
  }
</style>
</head>
<body>
  <article class="ad">
    <p class="tagline">KLARE WEGE</p>

    <h1 class="headline">
      <span class="question-lead">Was ist teurer als</span>
      <span class="question-key">Beratung?</span>
      <span class="answer">Ratlosigkeit!</span>
    </h1>

    <p class="intro">Wendholt &amp; Partner ist eine renommierte Management- und Personalberatung in Süddeutschland.</p>

    <section class="contact">
      <h2>KONTAKT</h2>
      <p>Wendholt &amp; Partner<br>Management- und Personalberatung AG<br>Gewerbehof Lindenau 14 | Alte Remise<br>76534 Talbrunn</p>
      <p>Tel.: +49 7000 4512-0<br>Fax: +49 7000 4512-90<br>info@wendholt-partner.de</p>
    </section>

    <div class="social" aria-label="Soziale Netzwerke">
      <span></span><span></span><span></span><span></span>
    </div>

    <svg class="footer-wave" viewBox="0 0 765 160" preserveAspectRatio="none" aria-hidden="true">
      <path d="M0 30 C 200 40, 450 70, 765 62 L765 160 L0 160 Z" fill="var(--wave-cream)" opacity="0.7"/>
      <path d="M0 42 C 220 60, 480 78, 765 74 L765 160 L0 160 Z" fill="var(--wave-pale)" opacity="0.8"/>
      <path d="M0 56 C 240 74, 500 92, 765 86 L765 160 L0 160 Z" fill="var(--paper)"/>
    </svg>

    <div class="brand">
      <span class="brand-mark"></span>
      <p class="brand-name">Wendholt &amp; Partner</p>
    </div>
    <p class="website">www.wendholt-partner.de</p>
  </article>
</body>
</html>
```